Become an EMT and Serve your community!

We are looking to design a postcard that will be mailed to surrounding communities that notifies them of our upcoming EMT class with an emphasis of serving their community. We are looking for a design that grabs peoples attention and motivates them to sign up and serve their community. Our primary colors are red and blue. We would like to incorporate the Institute logo as well as one or two photos. We do have more photos available upon request. Our Institute website is www.halvorsenacademy.net for more material. It is important that the postcard meets mailing guidelines.

Target Market(s)

Local community members

Industry/Entity Type

Education

Font styles to use
Sans Serif

Colors
f04a50
3176b5
0255a3
eaf1f7

Requirements
Must have
• Dates
Prices
Contact info
Look interesting
Convey the message of “Serving your Community”
Nice to have
• Clear information
Concise
Incorporate an action shot
Should not have
• Generic EMS logos

```html
<!DOCTYPE html>
<html lang="en">
<head>
<meta charset="utf-8">
<title>2020 Summer EMT Class Postcard</title>
<link rel="stylesheet" href="https://fonts.googleapis.com/css2?family=Montserrat:wght@800&family=Roboto:ital,wght@0,400;0,500;0,700;1,400;1,500&display=swap">
<style>
  :root {
    --red: #e9434c;
    --blue: #0255a3;
    --blue-mid: #3176b5;
    --navy: #1b2a6b;
    --page: #0b4dae;
    --panel: #e8eef7;
    --card-box: #f5f8fc;
    --paper: #f8f8f8;
    --ink: #333333;
    --white: #ffffff;
  }
  * { box-sizing: border-box; margin: 0; padding: 0; }
  html, body { width: 970px; height: 1200px; overflow: hidden; }
  body { background: var(--page); position: relative; font-family: "Roboto", sans-serif; }

  .postcard { position: absolute; left: 171px; width: 633px; overflow: hidden; }
  .postcard--front { top: 126px; height: 420px; background: var(--red); }
  .postcard--back { top: 637px; height: 417px; background: var(--paper); display: flex; }

  /* Front */
  .front-art { position: absolute; inset: 0; }
  .headline {
    position: absolute; left: 26px; top: 26px;
    font-family: "Montserrat", sans-serif; font-weight: 800;
    font-size: 35px; line-height: 34px; color: var(--white); letter-spacing: 0.2px;
  }
  .dots { position: absolute; left: 27px; top: 180px; display: flex; gap: 4px; }
  .dots span { width: 5px; height: 5px; border-radius: 50%; background: var(--white); }
  .intro {
    position: absolute; left: 25px; top: 203px; width: 225px;
    font-style: italic; font-weight: 500; font-size: 11.4px; line-height: 14px; color: var(--white);
  }
  .partners { position: absolute; left: 28px; top: 336px; display: flex; flex-direction: column; gap: 12px; }
  .partner { display: flex; align-items: center; gap: 8px; color: var(--white); font-weight: 700; font-size: 12px; }
  .partner-dot { width: 16px; height: 16px; border-radius: 50%; background: var(--navy); }

  /* Back */
  .details { width: 342px; height: 100%; background: var(--panel); padding: 27px 30px 0 29px; color: var(--ink); }
  .season { font-size: 19px; font-weight: 400; line-height: 22px; margin-left: 2px; }
  .title { font-size: 41px; font-weight: 700; line-height: 40px; letter-spacing: -0.3px; }
  .section-head { display: flex; align-items: center; gap: 5px; margin-top: 20px; }
  .section-head h2 { font-size: 15px; font-weight: 700; }
  .section-head .rule { flex: 1; height: 1px; background: #8a8f96; }
  .section-icon {
    width: 22px; height: 22px; border-radius: 50%; background: var(--card-box);
    display: flex; align-items: center; justify-content: center;
    font-size: 13px; font-weight: 700; color: var(--ink); margin-left: 3px;
  }
  .section-body { font-size: 11.4px; line-height: 14.5px; margin-top: 5px; }
  .note {
    background: var(--card-box); border-radius: 8px; margin-top: 14px;
    padding: 8px 9px; font-style: italic; font-size: 11.4px; line-height: 14.5px; height: 59px;
  }
  .note + .note { margin-top: 11px; }
  .tuition { margin-top: 14px; }

  .address-side { flex: 1; position: relative; }
  .stamp { position: absolute; left: 174px; top: 27px; width: 86px; height: 99px; border: 1.5px solid #1a1a1a; }
  .address-line { position: absolute; left: 29px; width: 231px; height: 1.5px; background: #1a1a1a; }
</style>
</head>
<body>

<section class="postcard postcard--front">
  <svg class="front-art" width="633" height="420" viewBox="0 0 633 420">
    <defs>
      <linearGradient id="labTone" x1="0" y1="0" x2="1" y2="1">
        <stop offset="0" stop-color="#cfc6b8"/>
        <stop offset="0.45" stop-color="#5b5a60"/>
        <stop offset="1" stop-color="#8c7f6a"/>
      </linearGradient>
      <linearGradient id="ambulanceTone" x1="0" y1="0" x2="1" y2="1">
        <stop offset="0" stop-color="#7d7f86"/>
        <stop offset="0.5" stop-color="#c9302c"/>
        <stop offset="1" stop-color="#e6d3c4"/>
      </linearGradient>
    </defs>
    <path d="M381 0 Q248 215 350 420 L633 420 L633 0 Z" fill="var(--blue)"/>
    <path d="M388 0 Q262 215 380 420 L633 420 L633 0 Z" fill="var(--white)"/>
    <path d="M393 0 Q272 215 410 420 L633 420 L633 0 Z" fill="url(#labTone)" role="img" aria-label="Photo: EMT students practising patient care on a training manikin on a stretcher"/>
    <circle cx="344" cy="304" r="96" fill="var(--white)"/>
    <circle cx="344" cy="304" r="92" fill="url(#ambulanceTone)" role="img" aria-label="Photo: two EMTs in red jackets treating a patient inside an ambulance"/>
  </svg>

  <h1 class="headline">Become<br>an EMT and<br>serve your<br>community!</h1>
  <div class="dots"><span></span><span></span><span></span></div>
  <p class="intro">Serve your community and become an Emergency Medical Technician. As a student you will have access to cutting edge training equipment, experienced instructors, and be able to train on a 911 Ambulance through Halvorsen EMS.</p>

  <div class="partners">
    <div class="partner"><span class="partner-dot"></span>Halvorsen Academy</div>
    <div class="partner"><span class="partner-dot"></span>Halvorsen Memorial EMS</div>
  </div>
</section>

<section class="postcard postcard--back">
  <div class="details">
    <p class="season">2020 Summer</p>
    <p class="title">EMT Class</p>

    <div class="section-head"><h2>When</h2><span class="rule"></span><span class="section-icon">?</span></div>
    <p class="section-body">Monday, Tuesday, Wednesday from May 26th<br>through August 17th.</p>

    <p class="note">Wednesdays: Students will need to sign up for either a 4:00p-7:00p lab section, of a 7:00p-10:0p lab section.</p>
    <p class="note">There will be one required Sat/Sun weekend held for all students. This will take place on June 13th &amp; 14th. Weekend classes will run from&nbsp; 8:00am - 8:00pm.</p>

    <div class="section-head tuition"><h2>Tuition</h2><span class="rule"></span><span class="section-icon">$</span></div>
    <p class="section-body">$1000 EMT (without CPR).<br>$250 deposit is due at time of registration.</p>
  </div>

  <div class="address-side">
    <div class="stamp"></div>
    <div class="address-line" style="top:212px"></div>
    <div class="address-line" style="top:244px"></div>
    <div class="address-line" style="top:276px"></div>
  </div>
</section>

</body>
</html>
```